Livestock Consulting Company has a logo but needs business cards and a uniform logo

My company works with farmers advising them on managing cattle and sheep. I have a logo but need business cards and a version of my logo to go onto my work shirts. I need the following wording added to my logo for my shirts "Marlowby Livestock Consulting".

```html
<!DOCTYPE html>
<html lang="en">
<head>
<meta charset="utf-8">
<title>Marlowby Livestock Consulting – Business Cards</title>
<link rel="stylesheet" href="https://fonts.googleapis.com/css2?family=Montserrat:wght@600&family=Arimo:wght@400;700&display=swap">
<style>
  :root {
    --bg: #2b2b2b;
    --card: #ffffff;
    --brown: #553f2b;
    --brown-mid: #6e5a46;
    --brown-logo: #5a4430;
    --ink-light: #ffffff;
    --shadow: rgba(0,0,0,0.45);
  }
  html, body { margin: 0; padding: 0; overflow: hidden; }
  body { width: 1200px; height: 900px; background: var(--bg); position: relative; }

  .card {
    position: absolute;
    left: 300px;
    width: 600px;
    height: 343px;
    background: var(--card);
    box-shadow: 0 10px 28px var(--shadow);
    overflow: hidden;
  }
  .card--front { top: 62px; }
  .card--back { top: 495px; }

  .wordmark {
    position: absolute;
    font-family: "Montserrat", sans-serif;
    font-weight: 600;
    color: var(--brown-logo);
    text-transform: uppercase;
    line-height: 1.15;
    display: flex;
    align-items: center;
    gap: 12px;
  }
  .wordmark__dot {
    width: 16px; height: 16px; border-radius: 50%;
    background: var(--brown-logo);
    flex: none;
  }
  .wordmark__text span { display: block; }
  .wordmark__sub { letter-spacing: 0.32em; }

  .card--front .wordmark { left: 0; right: 0; top: 120px; justify-content: center; font-size: 26px; }
  .card--front .wordmark__sub { font-size: 26px; text-align: center; }
  .front__web {
    position: absolute; left: 0; right: 0; top: 290px; text-align: center;
    font-family: "Arimo", sans-serif; font-size: 14px; letter-spacing: 0.06em; color: var(--brown);
  }

  .card--back .wordmark { left: 36px; top: 40px; font-size: 21px; }
  .card--back .wordmark__sub { font-size: 21px; }

  .back__art { position: absolute; inset: 0; }

  .holder {
    position: absolute; right: 28px; top: 160px; text-align: right;
    font-family: "Arimo", sans-serif; color: var(--ink-light);
  }
  .holder__name { font-size: 22px; font-weight: 700; }
  .holder__role { font-size: 12px; margin-top: 2px; }
  .holder__address { font-size: 13px; line-height: 1.55; margin-top: 16px; display: flex; gap: 8px; justify-content: flex-end; align-items: flex-start; }

  .contacts {
    position: absolute; left: 34px; top: 228px; margin: 0; padding: 0; list-style: none;
    font-family: "Arimo", sans-serif; font-size: 14px; color: var(--ink-light);
  }
  .contacts li { display: flex; align-items: center; gap: 16px; height: 22px; }
  .contacts svg { width: 14px; height: 14px; fill: none; stroke: var(--ink-light); stroke-width: 1.6; }
</style>
</head>
<body>

<section class="card card--front">
  <div class="wordmark">
    <div class="wordmark__text">
      <span>Marlowby Livestock</span>
      <span class="wordmark__sub">Consulting</span>
    </div>
  </div>
  <p class="front__web">www.marlowbylivestock.com</p>
</section>

<section class="card card--back">
  <svg class="back__art" viewBox="0 0 600 343" aria-hidden="true">
    <rect x="0" y="214" width="600" height="92" fill="var(--brown)"/>
    <path d="M600 150 H382 Q352 150 352 178 V196 Q352 214 372 220 L358 246 L398 222 Q412 214 430 214 V306 H600 Z" fill="var(--brown-mid)"/>
    <rect x="0" y="326" width="600" height="17" fill="var(--brown-mid)"/>
  </svg>

  <div class="wordmark">
    <div class="wordmark__text">
      <span>Marlowby Livestock</span>
      <span class="wordmark__sub">Consulting</span>
    </div>
  </div>

  <div class="holder">
    <div class="holder__name">Ravi Tolland</div>
    <div class="holder__role">Manager</div>
    <div class="holder__address">
      <span>14 Ashgrove Ln, Dunmore KS 67401,<br>Suite 12</span>
    </div>
  </div>

  <ul class="contacts">
    <li>
      <svg viewBox="0 0 16 16"><path d="M3 2 L6 2 L7 5 L5.5 6.5 Q7 9.5 9.5 10.5 L11 9 L14 10 L14 13 Q8 14 4 9 Q2 6 3 2 Z"/></svg>
      015 2468 1350
    </li>
    <li>
      <svg viewBox="0 0 16 16"><rect x="4" y="1.5" width="8" height="13" rx="1.5"/><line x1="7" y1="12" x2="9" y2="12"/></svg>
      015 2468 1350
    </li>
    <li>
      <svg viewBox="0 0 16 16"><rect x="1.5" y="3.5" width="13" height="9"/><path d="M1.5 3.5 L8 9 L14.5 3.5"/></svg>
      info@marlowbylivestock.com
    </li>
  </ul>
</section>

</body>
</html>
```